website in progress for new building development

Hi,
I have a new real estate development website in making but am running out of time for its completion. It's for a new apartment building for sales. Would it be possible for you to change/alter the site according to my requirements? I could send you all the existing files. The bulk of the website is done.
The images aren't really ready yet but will be within the next days so those will need to be replaced. Currently draft images are the placeholder on the website.

Let me know if you would be interested so we can quickly pick up correspondence.

This is the website so far (using Wordpress):
http://lindmoor.com.au/lindmoor/

Our domain is:
lindmoor.com.au

I am also adding the theme I am using.

Thanks.

Target Market(s)

Potential buyers.

Industry/Entity Type

Real Estate Development

Number of Pages Required

5+ page

Font styles to use
Other font styles liked:
• I used Robot under google fonts for the headlines

Requirements
Must have
• This is the current website
• http://lindmoor.com.au/lindmoor
• I'd like the colour scheme to remain the way it is.
• 1. Header
• I would like the header to have the menu on the right and have the 'Reigster' button similar to this website: (see the header here which shows up once you scroll down in the page) http://zenithbyfalconhouse.com.au/
• Please adjust this feature into our website with the menu items given.
• 2. Logo on Homepage
• Add the lindmoor logo into the top center of the feature image.
• Though permanent images are yet to arrive in the next few days. These are only drafts.
• 3. Footer
• Not sure about the colour scheme here yet.
• Should contain Disclaimer and copyrights.
• 4.Pages:
• a) Home
• b) Building
• c) Interior
• d) Location
• e) Register
• 5. page 'Home'
• When you scroll down in lindmoor.com.au/lindmoor/ you see the three images under the feature image, I would like those being hyperlinked as a 'box' just like this website has them when you scroll down here:
• http://www.velmotide.com.au/
• 6. page 'Register'
• I like the subtle colour scheme for the form used here http://zenithbyfalconhouse.com.au/#enquire-now
• and their 'Submit' button. Maybe adjust it to my website and remove the borders in the fields.
• 7. page 'Building'
• Will have two images of the exterior of the building which should be sliding automatically. (Images will be provided soon. For now I am only attaching draft images.)
• 8. page 'Interior'
• Will also have two images of the interior which should be automatically sliding. (Images will be provided soon. Attaching draft images for now)
Nice to have
• A language selection in the top right corner of each page:
• selection between english, mandarin, cantonese, korean.

```html
<!DOCTYPE html>
<html lang="en">
<head>
<meta charset="utf-8">
<title>Lindmoor — Register Now</title>
<link href="https://fonts.googleapis.com/css2?family=Open+Sans:wght@400;600&family=Roboto:wght@500;700&display=swap" rel="stylesheet">
<style>
  :root {
    --black: #000000;
    --page-bg: #edebeb;
    --footer-bg: #2c2c2c;
    --gold: #a8844b;
    --gold-light: #c9a15a;
    --icon-gold: #d4a04c;
    --heading: #3c3c3c;
    --text: #555555;
    --label: #5f5f5f;
    --field: #ffffff;
    --field-line: #dcdcdc;
    --white: #ffffff;
  }
  * { box-sizing: border-box; margin: 0; padding: 0; }
  html, body { width: 1200px; height: 765px; overflow: hidden; background: var(--page-bg); }
  body { font-family: "Open Sans", Arial, sans-serif; color: var(--text); }

  .site { position: relative; width: 1200px; height: 765px; overflow: hidden; }

  /* Header */
  .site-header { position: absolute; left: 0; top: 0; width: 1200px; height: 107px; background: var(--black); }
  .header-texture { position: absolute; inset: 0; background: linear-gradient(100deg, #000 0%, #141414 30%, #050505 55%, #161616 75%, #000 100%); }
  .brand { position: absolute; left: 99px; top: 72px; display: flex; align-items: center; gap: 8px; text-decoration: none; }
  .brand-mark { width: 10px; height: 10px; background: var(--gold-light); }
  .brand-name { font-family: "Open Sans", Arial, sans-serif; font-weight: 400; font-size: 15px; letter-spacing: 6px; color: var(--gold-light); }

  .main-nav { position: absolute; top: 45px; left: 479px; display: flex; gap: 32px; }
  .main-nav a { font-family: "Roboto", Arial, sans-serif; font-weight: 700; font-size: 14.5px; letter-spacing: 1.3px; color: var(--white); text-decoration: none; }

  .register-button { position: absolute; left: 890px; top: 35px; width: 126px; height: 40px; background: var(--gold); color: var(--white);
    font-family: "Roboto", Arial, sans-serif; font-weight: 700; font-size: 14.5px; letter-spacing: 1.3px;
    display: flex; align-items: center; justify-content: center; border-radius: 2px; text-decoration: none; }

  .language-select { position: absolute; left: 1034px; top: 35px; width: 68px; height: 39px; border: 1px solid #9a9a9a; border-radius: 3px;
    display: flex; align-items: center; gap: 10px; padding-left: 10px; }

  /* Main */
  .register-section { position: absolute; left: 0; top: 107px; width: 1200px; height: 559px; }
  .section-title { position: absolute; top: 56px; width: 100%; text-align: center; font-family: "Roboto", Arial, sans-serif;
    font-weight: 700; font-size: 29px; letter-spacing: 2.4px; color: var(--heading); }

  .office { position: absolute; left: 96px; width: 340px; }
  .office-north { top: 140px; }
  .office-south { top: 346px; }
  .office-name { font-weight: 600; font-size: 13.7px; color: #3e3e3e; margin-bottom: 22px; }
  .office-line { position: relative; padding-left: 34px; font-size: 13px; line-height: 26px; color: var(--text); }
  .office-line svg { position: absolute; left: 3px; }
  .office-address { margin-bottom: 12px; }
  .office-address svg { top: 4px; }
  .office-phone { margin-bottom: 13px; padding-left: 39px; }
  .office-phone svg { top: 3px; }
  .office-email { padding-left: 43px; }
  .office-email svg { top: 7px; }
  .office-email a { color: var(--text); text-decoration: underline; }

  .enquiry-form { position: absolute; left: 516px; top: 140px; width: 586px; }
  .field-row { display: flex; gap: 21px; }
  .field { display: block; width: 100%; margin-bottom: 14px; }
  .field-label { display: block; font-size: 11.5px; color: var(--label); text-transform: uppercase; margin-bottom: 11px; }
  .field-input { display: block; width: 100%; height: 34px; background: var(--field); border: 1px solid var(--field-line); }
  .field-select { position: relative; }
  .field-select::after { content: ""; position: absolute; right: 0; top: 0; width: 33px; height: 100%; border-left: 1px solid var(--field-line);
    background: linear-gradient(#f7f7f7, #e4e4e4); }
  .select-caret { position: absolute; right: 12px; top: 14px; z-index: 1; }
  .submit-button { margin-top: 19px; margin-left: 2px; width: 98px; height: 38px; background: var(--gold); color: var(--white); border: none; border-radius: 2px;
    font-family: "Open Sans", Arial, sans-serif; font-weight: 600; font-size: 13.5px; letter-spacing: 0.5px; }

  /* Footer */
  .site-footer { position: absolute; left: 0; top: 666px; width: 1200px; height: 99px; background: var(--footer-bg); }
  .footer-texture { position: absolute; inset: 0; background: linear-gradient(100deg, #2c2c2c 0%, #333 30%, #2a2a2a 55%, #343434 80%, #2c2c2c 100%); }
  .footer-text { position: absolute; top: 41px; width: 100%; text-align: center; font-size: 12px; color: var(--white); }
  .footer-text a { color: var(--white); text-decoration: none; }
  .footer-divider { margin: 0 7px; }
</style>
</head>
<body>
<div class="site">
  <header class="site-header">
    <div class="header-texture" role="img" aria-label="Faint dark geometric line pattern behind the header"></div>
    <a class="brand" href="#">
      <span class="brand-mark"></span>
      <span class="brand-name">LINDMOOR</span>
    </a>
    <nav class="main-nav">
      <a href="#">HOME</a>
      <a href="#">BUILDING</a>
      <a href="#">INTERIOR</a>
      <a href="#">LOCATION</a>
    </nav>
    <a class="register-button" href="#">REGISTER</a>
    <div class="language-select" aria-label="Language: English">
      <svg width="25" height="16" viewBox="0 0 60 30" aria-hidden="true">
        <rect width="60" height="30" fill="#012169"/>
        <path d="M0 0 L60 30 M60 0 L0 30" stroke="#fff" stroke-width="6"/>
        <path d="M0 0 L60 30 M60 0 L0 30" stroke="#C8102E" stroke-width="2"/>
        <path d="M30 0 V30 M0 15 H60" stroke="#fff" stroke-width="10"/>
        <path d="M30 0 V30 M0 15 H60" stroke="#C8102E" stroke-width="6"/>
      </svg>
      <svg width="10" height="6" viewBox="0 0 10 6" aria-hidden="true"><path d="M0 0 H10 L5 6 Z" fill="#fff"/></svg>
    </div>
  </header>

  <main class="register-section">
    <h1 class="section-title">REGISTER NOW</h1>

    <section class="office office-north">
      <h2 class="office-name">NORTH SYDNEY</h2>
      <p class="office-line office-address">
        <svg width="13" height="18" viewBox="0 0 13 18" aria-hidden="true"><path d="M6.5 0 C2.9 0 0 2.9 0 6.5 C0 11 6.5 18 6.5 18 C6.5 18 13 11 13 6.5 C13 2.9 10.1 0 6.5 0 Z M6.5 9 A2.5 2.5 0 1 1 6.5 4 A2.5 2.5 0 0 1 6.5 9 Z" fill="var(--icon-gold)"/></svg>
        Latin literature from 45 BC, making it over 2000<br>Brennick, at Tallowmere-Sydney
      </p>
      <p class="office-line office-phone">
        <svg width="17" height="17" viewBox="0 0 24 24" aria-hidden="true"><path d="M6.6 10.8 C8 13.6 10.4 16 13.2 17.4 L15.4 15.2 C15.7 14.9 16.1 14.8 16.5 14.9 C17.6 15.3 18.8 15.5 20 15.5 C20.6 15.5 21 15.9 21 16.5 V20 C21 20.6 20.6 21 20 21 C10.6 21 3 13.4 3 4 C3 3.4 3.4 3 4 3 H7.5 C8.1 3 8.5 3.4 8.5 4 C8.5 5.2 8.7 6.4 9.1 7.5 C9.2 7.9 9.1 8.3 8.8 8.6 Z" fill="var(--icon-gold)"/></svg>
        1 800 555 0142
      </p>
      <p class="office-line office-email">
        <svg width="21" height="15" viewBox="0 0 21 15" aria-hidden="true"><rect width="21" height="15" rx="1.5" fill="var(--icon-gold)"/><path d="M1 1.5 L10.5 8.5 L20 1.5" stroke="var(--page-bg)" stroke-width="1.5" fill="none"/></svg>
        <a href="#">info@lindmoor.in</a>
      </p>
    </section>

    <section class="office office-south">
      <h2 class="office-name">SOUTH SYDNEY</h2>
      <p class="office-line office-address">
        <svg width="13" height="18" viewBox="0 0 13 18" aria-hidden="true"><path d="M6.5 0 C2.9 0 0 2.9 0 6.5 C0 11 6.5 18 6.5 18 C6.5 18 13 11 13 6.5 C13 2.9 10.1 0 6.5 0 Z M6.5 9 A2.5 2.5 0 1 1 6.5 4 A2.5 2.5 0 0 1 6.5 9 Z" fill="var(--icon-gold)"/></svg>
        Latin literature from 45 BC, making it over 2000<br>Brennick, at Tallowmere-Sydney
      </p>
      <p class="office-line office-phone">
        <svg width="17" height="17" viewBox="0 0 24 24" aria-hidden="true"><path d="M6.6 10.8 C8 13.6 10.4 16 13.2 17.4 L15.4 15.2 C15.7 14.9 16.1 14.8 16.5 14.9 C17.6 15.3 18.8 15.5 20 15.5 C20.6 15.5 21 15.9 21 16.5 V20 C21 20.6 20.6 21 20 21 C10.6 21 3 13.4 3 4 C3 3.4 3.4 3 4 3 H7.5 C8.1 3 8.5 3.4 8.5 4 C8.5 5.2 8.7 6.4 9.1 7.5 C9.2 7.9 9.1 8.3 8.8 8.6 Z" fill="var(--icon-gold)"/></svg>
        1 800 555 0142
      </p>
      <p class="office-line office-email">
        <svg width="21" height="15" viewBox="0 0 21 15" aria-hidden="true"><rect width="21" height="15" rx="1.5" fill="var(--icon-gold)"/><path d="M1 1.5 L10.5 8.5 L20 1.5" stroke="var(--page-bg)" stroke-width="1.5" fill="none"/></svg>
        <a href="#">info@lindmoor.in</a>
      </p>
    </section>

    <form class="enquiry-form">
      <div class="field-row">
        <label class="field"><span class="field-label">First name :</span><span class="field-input"></span></label>
        <label class="field"><span class="field-label">Last name :</span><span class="field-input"></span></label>
      </div>
      <label class="field"><span class="field-label">Email :</span><span class="field-input"></span></label>
      <label class="field"><span class="field-label">Phone number :</span><span class="field-input"></span></label>
      <label class="field"><span class="field-label">What language would you prefer to be contacted in ?</span>
        <span class="field-input field-select">
          <svg class="select-caret" width="10" height="6" viewBox="0 0 10 6" aria-hidden="true"><path d="M0 0 H10 L5 6 Z" fill="#888"/></svg>
        </span>
      </label>
      <button class="submit-button" type="button">SUBMIT</button>
    </form>
  </main>

  <footer class="site-footer">
    <div class="footer-texture" role="img" aria-label="Faint geometric line pattern behind the footer"></div>
    <p class="footer-text">Copyright © 2015 Lindmoor. All rights reserved<span class="footer-divider">|</span><a href="#">Disclaimer</a></p>
  </footer>
</div>
</body>
</html>
```